Business Card Design

We would like a business card that utilizes our current logo and keeps with the same feel - elegant and organic. Our farm isn't about mass production, it's about excellence, education, beautiful events and flowers - people, culture, and community.

Target Market(s)

Patrons to our farm who are interested in weddings, events, or our flowers and vegetables.

Contact Information for Business Card

Name, address, cell email (Danielle Hoskins, 2716 Wrenfield Rd, Elk Bend, CO 80999, cell 555.412.6638, email danielle@wrenfieldacres.com)

```html
<!DOCTYPE html>
<html lang="en">
<head>
<meta charset="utf-8">
<title>Wrenfield Acres — Business Card</title>
<link href="https://fonts.googleapis.com/css2?family=Allison&family=Mulish:wght@400;500&display=swap" rel="stylesheet">
<style>
  :root{
    --bg:#e9e8e4;
    --card:#ffffff;
    --sage:#6f7e68;
    --copper:#b47642;
    --photo-light:#d9dccf;
    --photo-mid:#a9b09c;
    --photo-dark:#5c5f4a;
    --logo-light:#ffffff;
  }
  *{box-sizing:border-box;margin:0;padding:0}
  html,body{width:1200px;height:801px;overflow:hidden;background:var(--bg)}
  .canvas{position:relative;width:1200px;height:801px}
  .card{position:absolute;top:242px;width:555px;height:317px;border-radius:14px;overflow:hidden;
        box-shadow:0 6px 18px rgba(0,0,0,.12)}
  .card--front{left:30px}
  .card--back{left:615px;background:var(--card)}

  .front-photo{position:absolute;inset:0;
    background:linear-gradient(160deg,var(--photo-light) 0%,var(--photo-mid) 50%,var(--photo-dark) 100%)}
  .front-brand{position:absolute;left:0;right:0;top:50%;transform:translateY(-50%);
    text-align:center;font-family:'Mulish',sans-serif;font-weight:400;font-size:34px;
    letter-spacing:.12em;color:var(--logo-light)}

  .back-brand{position:absolute;right:40px;top:52px;font-family:'Mulish',sans-serif;
    font-weight:400;font-size:26px;letter-spacing:.1em;color:var(--sage)}
  .holder-name{position:absolute;left:46px;top:128px;font-family:'Allison',cursive;
    font-size:62px;line-height:1;color:var(--sage);white-space:nowrap}
  .holder-role{position:absolute;left:48px;top:192px;font-family:'Mulish',sans-serif;
    font-size:14px;font-weight:500;color:var(--copper)}
  .divider{position:absolute;left:46px;right:30px;top:218px;height:1px;background:var(--sage)}

  .contact{position:absolute;top:236px;list-style:none;font-family:'Mulish',sans-serif;
    font-size:13px;color:var(--copper)}
  .contact--left{left:46px}
  .contact--right{left:290px}
  .contact li{display:flex;align-items:center;gap:8px;height:26px;white-space:nowrap}
  .contact svg{width:13px;height:13px;fill:var(--sage);flex:none}
</style>
</head>
<body>
<div class="canvas">

  <section class="card card--front">
    <div class="front-photo" role="img" aria-label="Softly blurred photo of a long wedding reception table set with white linens, sage napkins and baby's breath bouquets"></div>
    <div class="front-brand">Wrenfield Acres</div>
  </section>

  <section class="card card--back">
    <div class="back-brand">Wrenfield Acres</div>
    <div class="holder-name">Danielle Hoskins</div>
    <div class="holder-role">CEO</div>
    <div class="divider"></div>

    <ul class="contact contact--left">
      <li>
        <svg viewBox="0 0 24 24" aria-hidden="true"><path d="M6.6 10.8a15.1 15.1 0 0 0 6.6 6.6l2.2-2.2a1 1 0 0 1 1-.25 11.4 11.4 0 0 0 3.6.6 1 1 0 0 1 1 1V20a1 1 0 0 1-1 1A17 17 0 0 1 3 4a1 1 0 0 1 1-1h3.5a1 1 0 0 1 1 1c0 1.25.2 2.45.6 3.6a1 1 0 0 1-.25 1z"/></svg>
        <span>555.412.6638</span>
      </li>
      <li>
        <svg viewBox="0 0 24 24" aria-hidden="true"><path d="M2 5h20v14H2zm2 2v.5l8 5 8-5V7z"/></svg>
        <span>danielle@wrenfieldacres.com</span>
      </li>
    </ul>

    <ul class="contact contact--right">
      <li>
        <svg viewBox="0 0 24 24" aria-hidden="true"><path d="M12 2a7 7 0 0 0-7 7c0 5.2 7 13 7 13s7-7.8 7-13a7 7 0 0 0-7-7zm0 9.5A2.5 2.5 0 1 1 12 6.5a2.5 2.5 0 0 1 0 5z"/></svg>
        <span>2716 Wrenfield Rd, Elk Bend, CO 80999</span>
      </li>
      <li>
        <svg viewBox="0 0 24 24" aria-hidden="true"><path d="M12 2a10 10 0 1 0 0 20 10 10 0 0 0 0-20zm6.9 9h-3a15 15 0 0 0-1.3-5.6A8 8 0 0 1 18.9 11zM12 4.1c.9 1.3 1.7 3.6 1.9 6.9h-3.8c.2-3.3 1-5.6 1.9-6.9zM9.4 5.4A15 15 0 0 0 8.1 11h-3a8 8 0 0 1 4.3-5.6zM5.1 13h3a15 15 0 0 0 1.3 5.6A8 8 0 0 1 5.1 13zm6.9 6.9c-.9-1.3-1.7-3.6-1.9-6.9h3.8c-.2 3.3-1 5.6-1.9 6.9zm2.6-1.3a15 15 0 0 0 1.3-5.6h3a8 8 0 0 1-4.3 5.6z"/></svg>
        <span>www.wrenfieldacres.com</span>
      </li>
    </ul>
  </section>

</div>
</body>
</html>
```